PC & LAPTOP REPAIR site design custom wordpress theme

Need a wordpress theme that is customized and can be upgraded without losing content, look.

KO brightDOT we provide a fast affordable pc/ laptop service that comes to you. We aim to provide same day service. I can add most of the text content i need a working theme with 5 pages, my logo. I have provided the layout i am after. This is the orange image.
I have provided my logo, the colour and some words.
I need your design skills at the same time i'm very much after the layout of the orange images FILE 1/4/5 . But with my logo and my colours the blue and black.

5 buttons beneath header. The old , ABOUT US, CONTACT US, HELP, PAYMENT, EMPLOYMENT ? That lead to pages i can edit my self. And 2 or 3 flashing cheesy images where the old man is in layout picture. Preferable a family or attractive female pc technician? as if they exist. joke im sure they do.

Also a box on index page query or quote. That people can simple fill and email. a simple php script maybe? however im happy.

I want to be able to edit page text myself, upgrade wordpress not lose layout, (upgrade and editable page friendly) WITH my blue my logo, my blue color theme

1ST 4TH 5TH fileS ARE the layout im after .

2nd. My logo and theme and color to be used in the layout of file 1.

3rd. Just some text and swirls that might be useful.

Reason: Have to visit family in Western Australia. Will be back in Melbourne 4th December.

• My logo KO brightDOT
My colour scheme that exact blue, with grey, black or white.
Same layout as image provided.
Can be upgraded and editable text.
• mobile device happy?
• contact box quote or query?

```html
<!DOCTYPE html>
<html lang="en">
<head>
<meta charset="utf-8">
<title>KO brightDOT – PC &amp; Laptop Repair</title>
<link href="https://fonts.googleapis.com/css2?family=Open+Sans:wght@400;600;700&display=swap" rel="stylesheet">
<style>
:root{
  --blue:#0a66b3;
  --blue-dark:#08508f;
  --blue-light:#2f8fe0;
  --link:#1a74b8;
  --ink:#333;
  --muted:#777;
  --page:#f0f0f0;
  --card:#f4f4f4;
  --line:#c9c9c9;
  --grey-dark:#2e2e2e;
  --grey-mid:#5a5a5a;
}
*{box-sizing:border-box;margin:0;padding:0}
html,body{width:1019px;height:1200px;overflow:hidden}
body{background:var(--page);font-family:"Open Sans",Arial,sans-serif;color:var(--ink);position:relative}
a{text-decoration:none;color:inherit}
.sheet{position:absolute;left:19px;top:14px;width:981px;height:1113px;background:var(--card);border:1px solid #d3d3d3;border-radius:8px;box-shadow:0 1px 4px rgba(0,0,0,.2)}
.brand{position:absolute;left:40px;top:38px;display:flex;align-items:center;gap:10px}
.brand-mark{width:44px;height:44px;background:var(--blue)}
.brand-name{font-size:34px;font-weight:700;color:var(--blue);letter-spacing:-.5px}
.health{position:absolute;left:314px;top:50px;display:flex;align-items:center;gap:10px;font-size:23px;font-weight:700;color:var(--blue)}
.call{position:absolute;left:683px;top:40px;text-align:left}
.call strong{display:block;font-weight:400;font-size:20px;color:#222}
.call span{font-size:14px;color:#555}
.chat-btn{position:absolute;left:830px;top:84px;background:var(--blue);color:#fff;font-size:12.5px;padding:3px 10px;border-radius:2px}
.agent{position:absolute;left:891px;top:22px;width:84px;height:84px;border-radius:50%;background:radial-gradient(circle at 55% 45%,#e9c8ae,#b78a6c 60%,#222 100%);border:2px solid #fff}
.nav{position:absolute;left:35px;top:117px;width:950px;height:53px;background:linear-gradient(#1d7cc9,var(--blue-dark));border-radius:6px 6px 0 0;display:flex}
.nav a{color:#fff;font-weight:600;font-size:16px;display:flex;align-items:center;justify-content:center;border-right:1px solid rgba(0,0,0,.25);box-shadow:1px 0 0 rgba(255,255,255,.15)}
.nav a:last-of-type{border-right:0;box-shadow:none}
.hero{position:absolute;left:35px;top:170px;width:950px;height:334px;border:2px solid var(--blue-dark);border-top:0;border-radius:0 0 6px 6px;overflow:hidden;background:linear-gradient(90deg,#cfc8c0,#eee9e3 35%,#f6f6f6 55%,#c2bfbb 75%,#3a3530)}
.hero-caption{position:absolute;right:0;bottom:14px;width:720px;height:46px;background:rgba(40,40,40,.65);color:#fff;font-size:23px;display:flex;align-items:center;justify-content:flex-end;padding-right:52px}
.news{position:absolute;left:34px;top:525px;width:254px;height:252px;border-radius:5px;background:linear-gradient(var(--grey-mid),var(--grey-dark));color:#fff;padding:12px 16px}
.panel-title{font-size:19px;font-weight:700;display:flex;align-items:center;gap:8px;text-transform:uppercase}
.panel-title i{width:22px;height:16px;background:var(--blue);display:inline-block}
.news-item{margin-top:10px}
.news-date{color:var(--blue-light);font-weight:700;font-size:14px}
.news-text{font-size:13px;line-height:16px}
.news-more{color:#7ab8ec;font-size:11px;margin-top:6px;display:block}
.btn{display:inline-block;background:var(--blue);color:#fff;font-weight:600;font-size:14px;padding:5px 10px;border-radius:2px}
.news .btn{margin-top:12px}
.booking{position:absolute;left:34px;top:797px;width:254px;height:315px;border-radius:5px;background:linear-gradient(#1472c2,var(--blue-dark));padding:10px 14px;color:#fff}
.booking .panel-title{margin-bottom:8px}
.field{height:28px;border:2px solid #5ea6e4;border-radius:3px;background:var(--blue-dark);font-size:13px;padding:4px 9px;margin-bottom:7px;box-shadow:inset 0 1px 2px rgba(0,0,0,.5)}
.field.area{height:86px}
.send{background:linear-gradient(#666,#333);font-weight:400;padding:3px 10px;margin-top:0}
.welcome{position:absolute;left:308px;top:524px;width:677px}
.welcome h2{font-size:19px;font-weight:700;color:#333;display:flex;align-items:baseline;gap:8px;padding-bottom:8px;border-bottom:1px solid #8bb9de;width:652px}
.welcome h2 b{color:var(--blue);font-size:18px}
.welcome p{font-size:11.4px;line-height:17.6px;color:#333;margin-top:7px;letter-spacing:-.05px}
.welcome p+p{margin-top:0}
.read-more{display:block;text-align:right;color:var(--link);font-size:12px;margin-top:4px}
.services{position:absolute;left:308px;top:798px;width:677px;height:314px;border:1px solid #bbb;border-radius:6px;background:#efefef;overflow:hidden}
.services-head{height:41px;background:linear-gradient(#136fbd,var(--blue-dark));color:#fff;font-size:19px;font-weight:700;padding:8px 14px}
.service-grid{display:grid;grid-template-columns:1fr 1fr;row-gap:25px;padding:14px 14px 0}
.service{display:flex;gap:15px}
.thumb{width:97px;height:66px;border:1px solid var(--blue);flex:none;background:linear-gradient(135deg,#eee,#8a8f96 60%,#333)}
.service h3{font-size:14px;font-weight:400;color:var(--link);margin-top:1px}
.service p{font-size:11.4px;line-height:17.6px;margin-top:7px;width:192px}
.service p em{color:var(--blue);font-style:normal;font-size:9px;margin-left:6px}
.footer{position:absolute;left:0;top:1148px;width:1019px;height:52px;background:#e6e6e6;border-top:1px solid #ddd}
.social{position:absolute;left:35px;top:12px;display:flex;gap:9px}
.social span{width:27px;height:27px;border-radius:50%;background:#9a9a9a;border:2px solid #ccc}
.social span:first-child{background:var(--blue)}
.copy{position:absolute;left:416px;top:19px;font-size:10.5px;color:#888}
.copy b{color:#555;font-weight:400}
.legal{position:absolute;right:16px;top:16px;font-size:12.5px;color:var(--blue-dark)}
</style>
</head>
<body>
<div class="sheet"></div>

<header>
  <a class="brand" href="#"><span class="brand-mark"></span><span class="brand-name">KO brightDOT</span></a>
  <a class="health" href="#">
    <svg width="26" height="26" viewBox="0 0 26 26"><circle cx="13" cy="13" r="12" fill="#fff"/><path d="M13 5v16M5 13h16" stroke="#0a66b3" stroke-width="4"/></svg>
    Book Your PC Health Check
  </a>
  <div class="call"><strong>Call us + 0400 555 123</strong><span>or chat with a technical expert</span></div>
  <a class="chat-btn" href="#">Chat Now</a>
  <div class="agent" role="img" aria-label="Photo of a support agent wearing a headset"></div>
</header>

<nav class="nav">
  <a href="#" style="width:127px">HOME</a>
  <a href="#" style="width:159px">ABOUT US</a>
  <a href="#" style="width:154px">PAYMENT</a>
  <a href="#" style="width:188px">EMPLOYMENT</a>
  <a href="#" style="width:117px">HELP</a>
  <a href="#" style="width:173px">CONTACT US</a>
</nav>

<section class="hero" role="img" aria-label="Slideshow photo of friendly technicians repairing a desktop computer">
  <div class="hero-caption">Having trouble connecting to the internet?</div>
</section>

<aside class="news">
  <div class="panel-title"><i></i>Latest News</div>
  <div class="news-item">
    <div class="news-date">28 October 2012</div>
    <div class="news-text">Lorem ipsum dolor sit amet, lorecoset-dipiscing elit.</div>
    <a class="news-more" href="#">READ MORE &raquo;</a>
  </div>
  <div class="news-item">
    <div class="news-date">28 October 2012</div>
    <div class="news-text">Lorem ipsum dolor sit amet, lorecose adipiscing elit.</div>
    <a class="news-more" href="#">READ MORE &raquo;</a>
  </div>
  <a class="btn" href="#">VIEW ALL NEWS</a>
</aside>

<form class="booking">
  <div class="panel-title">Book a Job</div>
  <div class="field">Fist Name</div>
  <div class="field">Last Name</div>
  <div class="field">Email</div>
  <div class="field">Contact Number</div>
  <div class="field area">How can we help?</div>
  <span class="btn send">SEND</span>
</form>

<section class="welcome">
  <h2>WELCOME <b>KO brightDOT</b></h2>
  <p>Lorem ipsum dolor sit amet, consectetur adipisicing elit, sed do eiusmod tempor incididunt ut labore et dolore magna aliqua. Ut enim ad minim veniam, quis nostrud exercitation ullamco laboris nisi ut aliquip ex ea commodo consequat. Duis aute irure dolor in reprehenderit in voluptate velit esse cillum dolore eu fugiat nulla pariatur. Excepteur sint occaecat cupid-atat non proident, sunt in culpa qui officia deserunt mollit anim id est laborum.</p>
  <p>Lorem ipsum dolor sit amet, consectetur adipisicing elit, sed do eiusmod tempor incididunt ut labore et dolore magna aliqua. Ut enim ad minim veniam, quis nostrud<br>exercitation ullamco laboris nisi ut aliquip ex ea commodo consequat. Duis aute irure dolor in reprehenderit in voluptate velit esse cillum dolore eu fugiat nulla pariatur.</p>
  <p>Lorem ipsum dolor sit amet, consectetur adipisicing elit, sed do eiusmod tempor incididunt ut labore et dolore magna aliqua. Ut enim ad minim veniam, quis nostrud exercitation ullamco laboris nisi ut aliquip ex ea commodo consequat. Duis autenulla pariatur. Excepteur sint occaecat cupidatat non proident, sunt in culpa qui officia deserunt mollit anim id est laborum.</p>
  <a class="read-more" href="#" style="margin-top:-14px">Read more &raquo;</a>
</section>

<section class="services">
  <div class="services-head">OUR SERVICES</div>
  <div class="service-grid">
    <div class="service"><div class="thumb" role="img" aria-label="Desktop computers and laptop"></div><div><h3>Lorem ipsum dolor sit amet</h3><p>Lorem ipsum dolor sit amet, cnsa-diicing elit, sed do eiusmod te<em>&#9654;</em></p></div></div>
    <div class="service"><div class="thumb" role="img" aria-label="Opened laptop with parts removed"></div><div><h3>Lorem ipsum dolor sit amet</h3><p>Lorem ipsum dolor sit amet, cnsa-diicing elit, sed do eiusmod te<em>&#9654;</em></p></div></div>
    <div class="service"><div class="thumb" role="img" aria-label="Monitor and tower computer"></div><div><h3>Lorem ipsum dolor sit amet</h3><p>Lorem ipsum dolor sit amet, cnsa-diicing elit, sed do eiusmod te<em>&#9654;</em></p></div></div>
    <div class="service"><div class="thumb" role="img" aria-label="Hard drive with a stethoscope"></div><div><h3>Lorem ipsum dolor sit amet</h3><p>Lorem ipsum dolor sit amet, cnsa-diicing elit, sed do eiusmod te<em>&#9654;</em></p></div></div>
    <div class="service"><div class="thumb" role="img" aria-label="Technician working inside a computer case"></div><div><h3>Lorem ipsum dolor sit amet</h3><p>Lorem ipsum dolor sit amet, cnsa-diicing elit, sed do eiusmod te<em>&#9654;</em></p></div></div>
    <div class="service"><div class="thumb" role="img" aria-label="Laptop beside an open computer with tools"></div><div><h3>Lorem ipsum dolor sit amet</h3><p>Lorem ipsum dolor sit amet, cnsa-diicing elit, sed do eiusmod te<em>&#9654;</em></p></div></div>
  </div>
</section>

<footer class="footer">
  <div class="social" aria-label="Social links"><span></span><span></span><span></span><span></span><span></span><span></span></div>
  <div class="copy">&copy; 2012 <b>ko bright dot</b>. All rights reserved.</div>
  <div class="legal"><a href="#">Privacy Policy</a> &nbsp;|&nbsp; <a href="#">Terms Of Service</a></div>
</footer>
</body>
</html>
```